Awesome Dessert Baker needs Sticker Design

My wife is an incredible baker. She specializes in desserts and everyone that tastes her baked goods has told her to start selling them. She recently decided to go into business and just through word of mouth and her reputation she is already getting steady orders.

She is looking to have a sticker developed to put on her cake boxes and packaging.

She wants the following:
1. Colors to be used- hot pink, purple, white
2. Want a sleek, modern design and style incorporating following:
name: Whisked by Nora
tel: 646 382 1074
email: nora@whiskedbynora.example

**no old fashion baking references like rolling pins, aprons, ect.

We want the sticker to be very appealing and eye catching that will further promote her image and business.

Industry/Entity Type

Fashion

Requirements
Must have
• Must contain the following information:

Whisked by Nora
646 382 1074 (please make small and discreet)
nora@whiskedbynora.example (please make small and discreet)
Should not have
• **no old fashion baking references like rolling pins, aprons, ect.

```html
<!DOCTYPE html>
<html lang="en">
<head>
<meta charset="utf-8">
<title>Whisked by Nora — Sticker</title>
<link rel="stylesheet" href="https://fonts.googleapis.com/css2?family=Open+Sans:wght@400;600&display=swap">
<style>
  :root {
    --backdrop: #efe7de;
    --sticker-white: #ffffff;
    --lilac: #b864d4;
    --ribbon-purple: #6c1f80;
    --ribbon-fold: #4d1460;
    --type-white: #ffffff;
  }
  html, body {
    margin: 0;
    padding: 0;
    width: 1200px;
    height: 900px;
    overflow: hidden;
    background: var(--backdrop);
  }
  .canvas {
    position: relative;
    width: 1200px;
    height: 900px;
  }
  .sticker {
    position: absolute;
    left: 0;
    top: 0;
    width: 1200px;
    height: 900px;
  }
  .sticker-base { fill: var(--sticker-white); }
  .badge { fill: var(--lilac); }
  .ribbon { fill: var(--ribbon-purple); }
  .ribbon-fold { fill: var(--ribbon-fold); }
  .brand-name, .contact {
    fill: var(--type-white);
    font-family: "Open Sans", sans-serif;
  }
  .brand-name {
    font-size: 62px;
    font-weight: 400;
    letter-spacing: 1px;
  }
  .contact { font-weight: 600; }
  .contact-phone { font-size: 28px; letter-spacing: 4px; }
  .contact-email { font-size: 24px; letter-spacing: 1.5px; }
</style>
</head>
<body>
<main class="canvas">
  <svg class="sticker" viewBox="0 0 1200 900" xmlns="http://www.w3.org/2000/svg">
    <circle class="sticker-base" cx="600" cy="450" r="350"/>
    <circle class="badge" cx="600" cy="445" r="298" role="img" aria-label="Lace doily with cut-out pattern"/>

    <text class="brand-name" x="600" y="430" text-anchor="middle">Whisked by Nora</text>

    <g class="ribbons" transform="rotate(-15 630 600)">
      <polygon class="ribbon-fold" points="890,560 925,560 905,580"/>
      <polygon class="ribbon" points="325,545 945,545 945,615 325,615 345,580"/>
      <polygon class="ribbon-fold" points="390,615 420,615 420,635"/>
      <polygon class="ribbon" points="390,630 930,630 915,660 930,690 390,690"/>
    </g>

    <g class="contacts" transform="rotate(-15 630 600)">
      <text class="contact contact-phone" x="640" y="591" text-anchor="middle">646 382 1074</text>
      <text class="contact contact-email" x="662" y="669" text-anchor="middle">nora@whiskedbynora.example</text>
    </g>
  </svg>
</main>
</body>
</html>
```